K & D A/C Compressors' Business Card

Hello,

I need someone to create a new business card for my business. The name of my Business is: K & D A/C Compressors. I sell automotive air conditioning parts (a/c parts). I would like the business card to incorporate my logo, and to have an automotive feel to it. It is important that the business card feel like it is coming from an automotive parts business.

I already have a logo, which I will provide.

Thanks.
Updates

Project Deadline Extended Reason: I feel like extending the deadline until October 9, 2017, will allow for more time to design the business card. Thank you for your understanding. Added Monday, October 2, 2017

Target Market(s)

Consumers who need automotive a/c parts, and auto mechanics.

Industry/Entity Type

Automotive

Contact Information for Business Card

Business name: K & D A/C Compressors
Business Address: 48207 Southwest 36th Street, North Miami Beach, Florida 33162
Telephone: 305-472-1390
Fax: To be provided once I choose your design.
Website: www.kdcoolunits.example
Email: support@kdcoolunits.example
Names: To be provided once I choose your design.

Font styles to use
Sans Serif

Colors

Designer to choose colors to be used in the design.

Requirements
Must have
• The business card must include all of the "Business Card Details" and the logo I have uploaded.

```html
<!DOCTYPE html>
<html lang="en">
<head>
<meta charset="utf-8">
<title>K &amp; D A/C Compressors – Business Card</title>
<link href="https://fonts.googleapis.com/css2?family=Roboto:wght@300;400&family=Roboto+Condensed:wght@400&display=swap" rel="stylesheet">
<style>
  :root {
    --bg: #2a2a2a;
    --card-white: #f4f4f4;
    --brand-blue: #05a6e4;
    --logo-grey: #9d9d9d;
    --text-dark: #454545;
    --text-mid: #8e8e8e;
    --rule: #c9c9c9;
    --white: #ffffff;
  }
  * { margin: 0; padding: 0; box-sizing: border-box; }
  html, body { width: 1200px; height: 960px; overflow: hidden; }
  body {
    background: var(--bg);
    position: relative;
    font-family: "Roboto", Arial, sans-serif;
  }
  .card {
    position: absolute;
    width: 600px;
    height: 342px;
    box-shadow: 0 2px 6px rgba(0,0,0,.45);
  }
  .card--front { left: 314px; top: 113px; background: var(--card-white); overflow: hidden; }
  .card--back { left: 311px; top: 472px; background: var(--brand-blue); }

  .front__band {
    position: absolute; left: 0; right: 0; bottom: 0; height: 15px;
    background: var(--brand-blue);
    border-top: 3px solid var(--rule);
  }
  .front__divider {
    position: absolute; left: 296px; top: 82px; width: 2px; height: 186px;
    background: linear-gradient(to bottom, rgba(150,150,150,0), #9a9a9a 20%, #9a9a9a 80%, rgba(150,150,150,0));
  }
  .wordmark {
    position: absolute; font-family: "Roboto", Arial, sans-serif; font-weight: 300;
    text-align: center; line-height: 1;
  }
  .wordmark__main { display: block; letter-spacing: 2px; }
  .wordmark__sub { display: block; }
  .front__wordmark { left: 32px; width: 240px; top: 128px; color: var(--logo-grey); }
  .front__wordmark .wordmark__main { font-size: 46px; }
  .front__wordmark .wordmark__sub { font-size: 25px; margin-top: 10px; }

  .contact { position: absolute; left: 321px; top: 84px; color: var(--text-dark); }
  .contact__name {
    font-family: "Roboto Condensed", Arial, sans-serif; font-size: 24px;
    color: var(--brand-blue); line-height: 1; text-transform: uppercase;
  }
  .contact__title {
    font-family: "Roboto Condensed", Arial, sans-serif; font-size: 15px;
    color: var(--text-mid); margin-top: 4px; text-transform: uppercase;
  }
  .contact__address { font-size: 14.5px; line-height: 18px; margin-top: 6px; }
  .contact__list { list-style: none; margin-top: 10px; }
  .contact__item { display: flex; align-items: center; font-size: 14.5px; line-height: 19.3px; }
  .contact__icon { width: 14px; height: 14px; margin-right: 9px; fill: var(--brand-blue); flex: none; }

  .back__wordmark { left: 0; right: 0; top: 118px; color: var(--white); }
  .back__wordmark .wordmark__main { font-size: 60px; font-weight: 300; }
  .back__wordmark .wordmark__sub { font-size: 34px; margin-top: 12px; }
  .back__web {
    position: absolute; left: 0; right: 0; top: 282px; text-align: center;
    color: var(--white); font-size: 14px; letter-spacing: 4.6px; font-weight: 400;
  }
</style>
</head>
<body>
  <section class="card card--front" aria-label="Business card front">
    <div class="wordmark front__wordmark">
      <span class="wordmark__main">K &amp; D</span>
      <span class="wordmark__sub">A/C Compressors</span>
    </div>
    <div class="front__divider"></div>
    <div class="contact">
      <p class="contact__name">Daniel Reyes</p>
      <p class="contact__title">CEO/Founder</p>
      <p class="contact__address">48207 Southwest 36th Street<br>North Miami Beach, Florida 33162</p>
      <ul class="contact__list">
        <li class="contact__item">
          <svg class="contact__icon" viewBox="0 0 16 16" aria-hidden="true"><path d="M3.2 1.5l2.3-.4 1.4 3.3-1.6 1.2c.8 1.8 2.1 3.1 3.9 3.9l1.2-1.6 3.3 1.4-.4 2.3c-.2.9-1 1.4-1.9 1.3C6.2 12.3 2.5 8.6 1.9 3.4c-.1-.9.4-1.7 1.3-1.9z"/></svg>
          305-472-1390
        </li>
        <li class="contact__item">
          <svg class="contact__icon" viewBox="0 0 16 16" aria-hidden="true"><path d="M4 1h8v4H4z M1 6h14v6h-2v-2H3v2H1z M4 11h8v4H4z"/></svg>
          305-472-1391
        </li>
        <li class="contact__item">
          <svg class="contact__icon" viewBox="0 0 16 16" aria-hidden="true"><path d="M1 3h14v1.2L8 8.6 1 4.2z M1 5.8l7 4.4 7-4.4V13H1z"/></svg>
          support@kdcoolunits.example
        </li>
        <li class="contact__item">
          <svg class="contact__icon" viewBox="0 0 16 16" aria-hidden="true"><circle cx="8" cy="8" r="7"/><path d="M5 4c1.5.5 2 1.5 1.5 2.5S4 7 4.5 8.5 6 10 6 12" stroke="#f4f4f4" stroke-width="1.3" fill="none"/><path d="M10 3.5c-.5 1 .5 2 1.5 2.3" stroke="#f4f4f4" stroke-width="1.3" fill="none"/></svg>
          www.kdcoolunits.example
        </li>
      </ul>
    </div>
    <div class="front__band"></div>
  </section>

  <section class="card card--back" aria-label="Business card back">
    <div class="wordmark back__wordmark">
      <span class="wordmark__main">K &amp; D</span>
      <span class="wordmark__sub">A/C Compressors</span>
    </div>
    <p class="back__web">www.kdcoolunits.example</p>
  </section>
</body>
</html>
```